This will be a design for publicity materials for an event:

DEBATE: That the NMC will harm Asia's growing digital economies

Date: 18 July 2013, 19:00-21:00
Venue: Function Room 6, Level 3, The Orchid Valehouse, Kota Kinabalu, Malaysia
RSVP: to marcus@velbrinex.org by 11 July 2013, limited free tickets available

- blurb begins -

The Northern Meridian Compact offers a golden opportunity for Asian nations to reap the rich rewards of global trade - or else it poses a dire threat to their sovereignty that would allow foreign multinational corporations to rewrite national laws for their own benefit. Opinions about the merits of the Northern Meridian Compact for Asia are polarised, making it difficult for ordinary citizens to separate fact from fiction. So what better topic for a debate, to clear the air and shed some light on this impenetrable and controversial subject?

Patron Guild Worldwide, in partnership with Byteline Report Hub, is hosting a free public 3-on-3 parliamentary-style debate on the proposition "That the NMC will harm Asia's growing digital economies". Drawn from across the region's government, industry and NGO communities, the participants will attempt to convince the audience that the NMC is the best hope for stimulating growth and innovation in Asia's high-tech industries - or that it will hamstring those industries with inappropriate laws pushed by foreign interests. Who wins? The audience will decide.

- blurb ends -

We want to have a design in 4 formats to promote this online, but you can just do one format to respond to the brief, and the others can come after I select a winner. One of the formats should be suitable to be emailed, so you could do it either as a graphic, or else as an HTML page suitable for emailing. The second format should be a 430 x 130 banner. Third should be a 300 x 250 banner. Also one format in about 800x600 or similar that we can use as a presentation slide at the venue.

Just to clarify, you don't need to include the whole blurb text.  Particularly in the small formats, that would be impossible.  It is mainly included as background for you.

I apologise for not getting back to you with comments and feedback - I had to travel to India and don't have proper Internet access here. I will get back to you as soon as I can. 

Target Market(s)

Business people, NGOs, diplomats

Industry/Entity Type

Industry

Requirements
Must have
• Sponsors' logos are attached.
Nice to have
• In at least the larger formats, we need to have space to show the names of the debaters. But we don't have those names yet, so for now it should say something like "Debating teams announced soon", with the facility to change it later when we do have the names. I had thought about maybe using a stage with a curtain drawn for the "coming soon" variant, and the curtains drawn back to reveal the names for the final variant. But I leave this to you.
Should not have
• Prefer if you don't use stock photos of people.

```html
<!DOCTYPE html>
<html lang="en">
<head>
<meta charset="utf-8">
<title>Debate: That the NMC will harm Asia's growing digital economies</title>
<link rel="stylesheet" href="https://fonts.googleapis.com/css2?family=Arimo:wght@400;700&family=Roboto+Condensed:wght@400;700&display=swap">
<style>
  :root {
    --navy-deep: #06223a;
    --navy-mid: #11466f;
    --navy-light: #2f6f9c;
    --debate-grey: rgba(150, 170, 185, 0.75);
    --white: #ffffff;
    --orange: #f7a600;
    --cyan: #35e3f2;
    --band: #000000;
    --badge: #ffffff;
    --badge-text: #1c3553;
  }
  * { margin: 0; padding: 0; box-sizing: border-box; }
  html, body { width: 1200px; height: 900px; overflow: hidden; background: var(--navy-deep); }
  .poster {
    position: relative;
    width: 1200px;
    height: 900px;
    overflow: hidden;
    font-family: "Arimo", Arial, sans-serif;
    color: var(--white);
    text-align: center;
  }
  .backdrop {
    position: absolute;
    inset: 0;
    background:
      radial-gradient(ellipse 70% 55% at 45% 40%, var(--navy-light) 0%, rgba(47,111,156,0) 70%),
      linear-gradient(160deg, var(--navy-mid) 0%, var(--navy-deep) 75%);
  }
  .content { position: absolute; inset: 0; }
  .kicker {
    position: absolute;
    top: 100px; left: 0; right: 0;
    font-size: 88px;
    letter-spacing: 40px;
    padding-left: 40px;
    color: var(--debate-grey);
    line-height: 1;
  }
  .motion {
    position: absolute;
    top: 222px; left: 0; right: 0;
    font-family: "Roboto Condensed", "Arial Narrow", sans-serif;
    font-weight: 700;
    line-height: 1;
    white-space: nowrap;
  }
  .motion-lead { font-size: 50px; }
  .motion-acronym { font-size: 82px; color: var(--orange); margin: 0 22px; }
  .motion-full { font-size: 28px; margin-right: 24px; }
  .motion-headline {
    position: absolute;
    top: 320px; left: 0; right: 0;
    font-family: "Roboto Condensed", "Arial Narrow", sans-serif;
    font-weight: 700;
    font-size: 86px;
    line-height: 1;
    white-space: nowrap;
  }
  .accent { color: var(--cyan); }
  .date {
    position: absolute;
    top: 466px; left: 0; right: 0;
    font-family: "Roboto Condensed", "Arial Narrow", sans-serif;
    font-size: 56px;
    line-height: 1;
  }
  .blurb {
    position: absolute;
    top: 552px; left: 0; right: 0;
    font-size: 29px;
    font-weight: 700;
    line-height: 42px;
  }
  .sponsors {
    position: absolute;
    top: 662px; left: 0; right: 0;
    display: flex;
    justify-content: center;
    gap: 24px;
    list-style: none;
  }
  .sponsor {
    width: 114px;
    height: 76px;
    background: var(--badge);
    border-radius: 6px;
    display: flex;
    align-items: center;
    justify-content: center;
    padding: 6px;
    font-size: 15px;
    font-weight: 700;
    line-height: 1.15;
    color: var(--badge-text);
  }
  .details {
    position: absolute;
    left: 0; right: 0; bottom: 0;
    height: 135px;
    background: var(--band);
    padding-top: 24px;
    font-size: 26px;
    font-weight: 700;
    line-height: 40px;
    white-space: nowrap;
  }
</style>
</head>
<body>
  <main class="poster">
    <div class="backdrop" role="img" aria-label="Dark blue world map background with a rising growth arrow sweeping up to the right"></div>
    <div class="content">
      <p class="kicker">DEBATE</p>
      <h1 class="motion">
        <span class="motion-lead">That the</span><span class="motion-acronym">NMC</span><span class="motion-full">(Northern Meridian Compact)</span><span class="motion-lead">will harm</span>
      </h1>
      <p class="motion-headline"><span class="accent">Asia's</span> growing digital <span class="accent">economies</span></p>
      <p class="date">18 July 2013, 19:00-21:00</p>
      <p class="blurb">The Northern Meridian Compact offers a golden opportunity for<br>Asian nations to reap the rich rewards of global trade</p>
      <ul class="sponsors" aria-label="Sponsors">
        <li class="sponsor">Patron Guild Worldwide</li>
        <li class="sponsor">Byteline Report Hub</li>
        <li class="sponsor">Open Terms Coalition</li>
      </ul>
      <footer class="details">
        <p>Venue: Function Room 6, Level 3, The Orchid Valehouse, Kota Kinabalu, Malaysia</p>
        <p>RSVP: to marcus@velbrinex.org by 11 July 2013, limited free tickets available</p>
      </footer>
    </div>
  </main>
</body>
</html>
```